Fresh Start Body Quest 2017 Poster

We are having a Fresh Start, Body Quest for 2017 at our fitness studio. We need a poster design using the template attached as a reference (Only reference). I have also included our Drovelux logo to put on the poster. Please DO NOT use the graphics in the flyer as we are expecting something much much better :-)
MUST HAVES:
- Size needed 11x17 with bleeding for printing
- .PSD File Format WITH LAYERS (CS3 Compatible)*** A MUST
- Use Drovelux Bootcamps Logo
- Use Information in the attached word doc

```html
<!DOCTYPE html>
<html lang="en">
<head>
<meta charset="utf-8">
<title>Fresh Start, Body Quest 2017 – Drovelux Bootcamps</title>
<link rel="stylesheet" href="https://fonts.googleapis.com/css2?family=Archivo+Black&family=Roboto+Condensed:wght@300;700&display=swap">
<style>
  :root {
    --paper: #eceef0;
    --sky: #6699cc;
    --sky-deep: #2f5f9e;
    --navy: #1d3559;
    --crimson: #c1272d;
    --tan: #b8875a;
    --sun: #fff200;
    --ink: #111111;
    --white: #ffffff;
  }
  * { margin: 0; padding: 0; box-sizing: border-box; }
  html, body { width: 776px; height: 1200px; overflow: hidden; background: var(--paper); }
  .poster {
    position: relative; width: 776px; height: 1200px; overflow: hidden;
    background: var(--paper);
    font-family: "Roboto Condensed", "Arial Narrow", sans-serif;
    color: var(--ink);
  }
  .hero-band { position: absolute; top: 0; left: 0; width: 776px; height: 560px; }
  .brand {
    position: absolute; top: 30px; right: 40px;
    display: flex; align-items: center; gap: 12px; white-space: nowrap;
    font-family: "Archivo Black", sans-serif; font-size: 26px; line-height: 1; color: var(--white);
  }
  .brand__square { width: 18px; height: 18px; background: var(--sun); flex: none; }
  .headline {
    position: absolute; top: 140px; left: 48px;
    font-family: "Archivo Black", sans-serif; line-height: 1; white-space: nowrap;
  }
  .headline__lead { display: block; font-size: 64px; color: var(--sun); letter-spacing: 1px; }
  .headline__sub { display: block; font-size: 76px; color: var(--white); margin-top: 14px; letter-spacing: 1px; }
  .tagline {
    position: absolute; top: 330px; left: 48px; width: 440px;
    color: var(--white); font-weight: 300; font-size: 28px; line-height: 38px;
  }
  .tagline__accent { font-weight: 700; font-size: 34px; color: var(--sun); }
  .prize { position: absolute; left: 520px; top: 300px; width: 220px; height: 220px; }
  .prize__text {
    position: absolute; left: 520px; top: 300px; width: 220px; height: 220px;
    display: flex; flex-direction: column; align-items: center; justify-content: center;
    transform: rotate(-8deg);
    font-weight: 700; line-height: 1; text-align: center; color: var(--white); font-size: 28px;
  }
  .prize__amount { color: var(--sun); font-size: 50px; margin-bottom: 4px; }
  .dates {
    position: absolute; top: 590px; left: 40px; width: 696px; height: 170px;
    background: var(--white); border-left: 10px solid var(--tan);
    padding: 13px 0 0 28px; font-size: 28px; line-height: 48px; font-weight: 300; white-space: nowrap;
  }
  .dates strong { font-weight: 700; color: var(--tan); }
  .offer {
    position: absolute; top: 790px; left: 0; width: 776px; height: 120px;
    background: var(--sun); color: var(--crimson);
    display: flex; flex-direction: column; align-items: center; justify-content: center;
    font-weight: 700; font-size: 30px; line-height: 44px; text-align: center;
  }
  .offer__price { color: var(--ink); font-size: 40px; }
  .finale {
    position: absolute; top: 950px; left: 0; width: 776px; height: 110px;
    background: var(--ink); color: var(--white);
    display: flex; align-items: center; justify-content: center; gap: 14px;
    font-weight: 700; font-size: 32px;
  }
  .finale__date { color: var(--sun); font-size: 48px; }
  .footer {
    position: absolute; top: 1131px; left: 0; width: 776px; height: 69px;
    background: var(--sky); color: var(--white);
    display: flex; align-items: center; justify-content: center;
    font-weight: 700; font-size: 24px; white-space: nowrap;
  }
</style>
</head>
<body>
<main class="poster">
  <svg class="hero-band" viewBox="0 0 776 560" aria-hidden="true">
    <polygon points="0,0 776,0 776,470 0,540" fill="var(--navy)"/>
    <polygon points="560,0 776,0 776,470 420,508" fill="var(--sky-deep)"/>
    <polygon points="0,528 776,458 776,470 0,540" fill="var(--crimson)"/>
  </svg>

  <div class="brand"><span class="brand__square"></span>Drovelux Bootcamps</div>

  <h1 class="headline">
    <span class="headline__lead">FRESH START,</span>
    <span class="headline__sub">BODY QUEST</span>
  </h1>

  <p class="tagline">In Just <span class="tagline__accent">6 Weeks,</span> Transform Your Body And Get In The Best Shape Of Your Life!</p>

  <svg class="prize" viewBox="0 0 220 220" aria-hidden="true">
    <circle cx="110" cy="110" r="106" fill="var(--white)"/>
    <circle cx="110" cy="110" r="98" fill="var(--crimson)"/>
  </svg>
  <div class="prize__text">
    <span class="prize__amount">$500</span>
    <span>CASH Prize</span>
    <span>for Winner!</span>
  </div>

  <div class="dates">
    <p><strong>Kick Off Meeting:</strong> Thursday, Jan 12th at 7:30 pm</p>
    <p><strong>Start Date:</strong> Tuesday, January 17th</p>
    <p><strong>End Date:</strong> Saturday, February 25th</p>
  </div>

  <p class="offer"><span>6 Weeks of Training, Nutrition, and</span><span>Coaching Starting at just <span class="offer__price">$99!</span></span></p>

  <div class="finale"><span>Finale Party</span><span class="finale__date">March 2nd</span></div>

  <footer class="footer">Visit www.droveluxbootcamps.com FOR MORE INFO</footer>
</main>
</body>
</html>
```